Website for ecommerce chili product website

I am starting a hot sauce and chili product company and I need help designing the site. I have a brief outline for what i would like, but I need help bringing that designer's touch to my rough sketch. Please find the rough sketch here of what i would like built.

https://app.plandrafta.example/QrTeLmWoPvBnXcYuKjHgFdSaZxCvBnMq/view/page/c7d21ee4b

Currently, I only have 6 pages designed, but more will need to be done for example, when the order is placed.

I total, I will need the following pages built:

Home page
Products page
Accounts page / login
Checkout page
Confirmation page
Blog page
Subscription page
About page

I would like the color scheme to compliment the colors in my logo files and feel free to use the other pictures throughout the site as you find appropriate. The site should be clean, minimalist and easy to navigate. The content in products section I will have to add in manually later, so only placeholders now are needed. But one particular feature i would like is a "heat indicator" where I can estimate how hot a sauce would be. This will also need to be configurable at a later date when i add in my products.

Some similar sites I like are the following:
https://rubyorchid.example/
https://tidewell.example/

Traffic will be generated mainly by mobile, but also via desktop, therefore both mobile and desktop focus should be applied.

Target Market(s)

20-50

Industry/Entity Type

Food / hot sauce

Coding

Coded - Design and coding required

Requirements
Must have
• Good mobile design

```html
<!DOCTYPE html>
<html lang="en">
<head>
<meta charset="utf-8">
<title>Ember Thistle Hot Sauce</title>
<link href="https://fonts.googleapis.com/css2?family=Varela+Round&family=Roboto:wght@700&display=swap" rel="stylesheet">
<style>
  :root {
    --ink: #1f1f1f;
    --white: #ffffff;
    --purple: #6f4a8e;
    --logo-purple: #4e1f7a;
    --gold: #e2a40d;
    --dot: #dedede;
    --black: #050505;
  }
  * { box-sizing: border-box; margin: 0; padding: 0; }
  html, body { width: 1200px; height: 2389px; overflow: hidden; }
  body {
    position: relative;
    background: var(--white);
    color: var(--ink);
    font-family: "Varela Round", sans-serif;
  }
  .abs { position: absolute; }
  .center { left: 0; width: 1200px; text-align: center; }

  /* header */
  .site-header { top: 0; left: 0; width: 1200px; height: 83px; background: var(--white); z-index: 3; }
  .nav-link { position: absolute; top: 33px; font-size: 15.5px; letter-spacing: .2px; color: var(--ink); text-decoration: none; }
  .brand-tab {
    position: absolute; left: 506px; top: 0; width: 200px; height: 118px;
    background: var(--white); border-radius: 0 0 100px 100px / 0 0 40px 40px;
    z-index: 4; text-align: center;
  }
  .brand-mark { display: block; margin: 10px auto 0; width: 40px; height: 40px; border-radius: 50%; background: var(--gold); }
  .brand-name { display: block; margin-top: 14px; font-size: 20px; color: var(--logo-purple); letter-spacing: .5px; }

  /* hero */
  .hero { top: 83px; left: 0; width: 1200px; height: 294px;
    background: linear-gradient(100deg, #4c6d2e 0%, #7d8f52 22%, #8d8676 42%, #9b927f 65%, #8a8170 100%); }
  .hero-title { left: 565px; top: 145px; font-size: 35px; line-height: 43px; color: var(--white); letter-spacing: .6px; }

  /* sections */
  .section-title { font-size: 44px; letter-spacing: .5px; color: var(--ink); }
  .product-photo { width: 237px; height: 237px; border-radius: 50%; top: 540px; }
  .product-name { top: 788px; width: 300px; text-align: center; font-size: 22px; }
  .product-text { top: 825px; width: 300px; text-align: center; font-size: 14px; line-height: 26px; }

  .dots { display: flex; gap: 8px; justify-content: center; }
  .dots span { width: 12px; height: 12px; border-radius: 50%; background: var(--dot); }
  .dots span.active { background: var(--gold); }

  .pill-button {
    display: flex; align-items: center; justify-content: center; gap: 12px;
    background: var(--gold); border-radius: 21px; color: var(--logo-purple);
    font-size: 15.5px; letter-spacing: .3px;
  }
  .pill-button .pip { width: 14px; height: 14px; border-radius: 50%; background: var(--logo-purple); }

  .story-band { top: 1100px; left: 0; width: 1200px; height: 360px; }

  .rare-card { top: 1642px; width: 250px; height: 326px; border-radius: 2px; }
  .rare-label { position: absolute; left: 0; bottom: 28px; width: 100%; text-align: center;
    font-family: "Roboto", sans-serif; font-weight: 700; font-size: 25px; color: var(--white); }

  .site-footer { top: 2080px; left: 0; width: 1200px; height: 309px; }
  .footer-links { top: 2174px; font-size: 15.5px; color: var(--white); word-spacing: 2px; }
  .footer-links .sep { margin: 0 16px; }
  .social { top: 2214px; display: flex; gap: 8px; justify-content: center; }
  .social span { width: 35px; height: 35px; border-radius: 50%; background: #3a3a3a; }
  .footer-note { font-size: 15px; color: var(--white); }
</style>
</head>
<body>

<header class="abs site-header">
  <a class="nav-link" style="left:111px">CHILI PRODUCTS</a>
  <a class="nav-link" style="left:323px">SPICY GIFTS</a>
  <a class="nav-link" style="left:733px">ACCOUNT</a>
  <a class="nav-link" style="left:889px">BLOG</a>
  <a class="nav-link" style="left:1010px">CONTACT</a>
</header>
<div class="brand-tab">
  <span class="brand-mark"></span>
  <span class="brand-name">EMBER THISTLE</span>
</div>

<section>
  <div class="abs hero" role="img" aria-label="Red chili pepper growing on a green plant against weathered wood"></div>
  <h1 class="abs hero-title" style="font-weight:400">GROWN AND PRODUCED<br>IN SWITZERLAND WITH<br>SIMPLE AND NATURAL<br>INGREDIENTS</h1>
</section>

<section>
  <h2 class="abs center section-title" style="top:460px;font-weight:400">DISCOVER OUR PRODUCTS</h2>

  <div class="abs product-photo" style="left:156px;background:radial-gradient(circle,#c42a3a,#8e1a26)" role="img" aria-label="Bundles of dried red chilies"></div>
  <div class="abs product-photo" style="left:482px;background:radial-gradient(circle,#e0b43a,#b0461e 70%,#4c2a14)" role="img" aria-label="Yellow, green and red habanero peppers"></div>
  <div class="abs product-photo" style="left:807px;background:radial-gradient(circle,#a9c9cc,#8ab1b6)" role="img" aria-label="Three long red chilies on a pale blue surface"></div>

  <h3 class="abs product-name" style="left:125px;font-weight:400">Nemo enim ipsam</h3>
  <h3 class="abs product-name" style="left:451px;font-weight:400">Nemo enim ipsam</h3>
  <h3 class="abs product-name" style="left:776px;font-weight:400">Nemo enim ipsam</h3>
  <p class="abs product-text" style="left:125px">Lorem ipsum dolor sit amet, conse<br>ctetur adipiscing elit, sed</p>
  <p class="abs product-text" style="left:451px">Lorem ipsum dolor sit amet, conse<br>ctetur adipiscing elit, sed</p>
  <p class="abs product-text" style="left:776px">Lorem ipsum dolor sit amet, conse<br>ctetur adipiscing elit, sed</p>

  <div class="abs center dots" style="top:924px"><span></span><span class="active"></span><span></span><span></span></div>

  <a class="abs pill-button" style="left:482px;top:980px;width:236px;height:41px"><span class="pip"></span>VIEW OUR PRODUCTS</a>
</section>

<section>
  <svg class="abs story-band" viewBox="0 0 1200 360" preserveAspectRatio="none" aria-hidden="true">
    <path fill="var(--purple)" d="M0 8 C120 22 260 30 420 26 C600 22 760 20 900 12 C1020 6 1120 6 1200 10 L1200 330 C1100 338 980 336 820 338 C660 340 520 346 380 340 C240 334 120 346 0 330 Z"/>
  </svg>
  <h2 class="abs center section-title" style="top:1232px;color:var(--white);font-weight:400">LEARN ABOUT OUR STORY</h2>
  <a class="abs pill-button" style="left:516px;top:1301px;width:168px;height:41px"><span class="pip"></span>READ MORE</a>
</section>

<section>
  <h2 class="abs center section-title" style="top:1518px;font-weight:400">RARE CHILIS</h2>
  <p class="abs center" style="top:1582px;font-size:17px">Discover our regional specialties only available as limited editions.</p>

  <div class="abs rare-card" style="left:147px;background:linear-gradient(180deg,#8fb43a,#4f7a1e 50%,#a24a1e 75%,#2e4a14)" role="img" aria-label="Orange chili ripening on a leafy plant">
    <span class="rare-label">Duis aute irure</span>
  </div>
  <div class="abs rare-card" style="left:476px;background:linear-gradient(160deg,#6c8a2c,#a83a2a 45%,#c9c2c4 60%,#7a3a24)" role="img" aria-label="Market sacks of red and green chilies">
    <span class="rare-label">Duis aute irure</span>
  </div>
  <div class="abs rare-card" style="left:803px;background:linear-gradient(180deg,#c53a2a,#e0883a 40%,#b84422 70%,#d2b46a)" role="img" aria-label="Colourful strings of peppers hanging at a market stall">
    <span class="rare-label">Duis aute irure</span>
  </div>

  <div class="abs center dots" style="top:2012px"><span></span><span class="active"></span><span></span><span></span></div>
</section>

<footer>
  <svg class="abs site-footer" viewBox="0 0 1200 309" preserveAspectRatio="none" role="img" aria-label="Dark background of chilies in a bowl">
    <defs>
    <radialGradient id="footerGlow" cx="0.5" cy="0.6" r="0.6">
      <stop offset="0" stop-color="#2a0e10"/>
      <stop offset="1" stop-color="var(--black)"/>
    </radialGradient>
    </defs>
    <path fill="url(#footerGlow)" d="M0 14 C160 4 300 18 420 12 C560 4 700 16 840 10 C980 4 1100 6 1200 16 L1200 309 L0 309 Z"/>
  </svg>
  <p class="abs center footer-links">Chilli Products<span class="sep">|</span>Spicy Gifts<span class="sep">|</span>Account<span class="sep">|</span>Blog<span class="sep">|</span>Contact</p>
  <div class="abs center social"><span></span><span></span><span></span></div>
  <p class="abs center footer-note" style="top:2271px">Zurich, Switzerland</p>
  <p class="abs center footer-note" style="top:2306px">© Copyrights 2023 Company name | All Rights Reserved</p>
</footer>

</body>
</html>
```